Medical Device Packaging Project 3 of 5

We are a medical device startup company needing packaging for a total of 5 device brands. This is posting 3 of 5 and the device name is "Venor"

Venor is an intraocular lens for use in cataract surgery. The target market is Chinese ophthalmologists. The box should be sophisticated and upmarket.

The company name is Tamsin Medica, I have included the logo in the uploaded files section. You should include the logo on the box.

I have uploaded a sample lens boxes from other companies that demonstrate the information needed to be contained on the box in terms of address, warnings, symbols, etc.

I have also uploaded the blank dieline of the boxes

You are welcome and encouraged to also submit to projects 1, 2, 4, and 5 as well. The same rules and expectations apply.

Requirements
Should not have
• Should not have any images of an eye or any bionic/futuristic feel to the design
• Note that the calvoptix box is for text reference only. You may use the lens image but the futuristic/bionic look is NOT what we are going for with this brand. It should be traditional upmarket medical device artwork.

```html
<!DOCTYPE html>
<html lang="en">
<head>
<meta charset="utf-8">
<title>Venor – Tamsin Medica Lens Box Panels</title>
<link rel="stylesheet" href="https://fonts.googleapis.com/css2?family=Montserrat:wght@500;600;700&family=Arimo:wght@400&display=swap">
<style>
  :root{
    --stage:#e9ebec;
    --stage-edge:#d3d6d8;
    --panel:#ffffff;
    --green-soft:#d8f1d9;
    --green-mid:#9fdea4;
    --green-text:#2f7d4a;
    --navy:#1d3f6e;
    --sky:#a9cde3;
    --ink:#2a2a2a;
    --lens-light:#f2f2f2;
    --lens-dark:#8d8d8d;
  }
  *{box-sizing:border-box;margin:0;padding:0}
  html,body{width:1200px;height:782px;overflow:hidden}
  body{
    background:radial-gradient(ellipse at 50% 40%, #f6f7f7 0%, var(--stage) 60%, var(--stage-edge) 100%);
    font-family:"Arimo", Arial, sans-serif;
    position:relative;
  }
  .panel{
    position:absolute;
    top:190px;
    width:500px;
    height:400px;
    background:
      radial-gradient(ellipse at 15% 8%, var(--green-soft) 0%, rgba(216,241,217,0) 45%),
      radial-gradient(ellipse at 80% 88%, var(--green-mid) 0%, rgba(159,222,164,0) 55%),
      var(--panel);
    box-shadow:0 18px 30px rgba(0,0,0,.18);
    overflow:hidden;
  }
  .panel--back{left:60px}
  .panel--front{left:640px}
  .pattern{
    position:absolute;right:0;bottom:0;width:62%;height:60%;
    background:linear-gradient(135deg, rgba(159,222,164,0) 0%, rgba(159,222,164,.45) 60%, rgba(120,205,130,.35) 100%);
  }
  .brand{
    position:absolute;left:28px;top:80px;
    display:flex;align-items:center;gap:8px;
  }
  .brand__ring{
    width:28px;height:28px;border-radius:50%;
    border:3px solid var(--sky);
  }
  .brand__name{
    font-family:"Montserrat", sans-serif;font-weight:600;
    font-size:15px;letter-spacing:1.5px;color:var(--navy);
  }
  .title{
    position:absolute;right:26px;top:34px;
    font-family:"Montserrat", sans-serif;font-weight:600;
    font-size:14px;line-height:19px;color:var(--green-text);
    text-align:right;letter-spacing:.4px;
  }
  .lens{
    position:absolute;border-radius:50%;
    background:radial-gradient(circle at 40% 35%, var(--lens-light) 0%, #c4c4c4 45%, var(--lens-dark) 80%, #555 100%);
    box-shadow:0 0 0 4px #b5b5b5;
  }
  .panel--back .lens{left:340px;top:140px;width:100px;height:100px}
  .panel--front .lens{left:210px;top:128px;width:176px;height:176px}
  .warnings{
    position:absolute;left:28px;top:150px;width:290px;
    font-size:6.8px;line-height:8px;color:var(--ink);
  }
  .warnings p{margin-bottom:3px}
  .symbols{
    position:absolute;right:26px;bottom:52px;
    display:flex;gap:9px;align-items:center;
  }
  .symbols svg{display:block}
  .sterile{
    border:1px solid var(--ink);font-size:6px;font-weight:700;
    font-family:"Montserrat", sans-serif;display:flex;
  }
  .sterile span{padding:2px 3px}
  .sterile span+span{border-left:1px solid var(--ink)}
  .product{
    position:absolute;left:34px;bottom:34px;color:var(--green-text);
    font-family:"Montserrat", sans-serif;
  }
  .product__name{font-size:22px;font-weight:700;letter-spacing:4px;line-height:24px}
  .product__type{font-size:14px;font-weight:600;letter-spacing:.4px}
</style>
</head>
<body>

<section class="panel panel--back" aria-label="Back panel">
  <div class="pattern"></div>
  <h2 class="title">HYDROPHOBIC INTRAOCULAR LENS<br>ASPHERIC WITH 360° LENS</h2>
  <div class="brand">
    <span class="brand__ring"></span>
    <span class="brand__name">TAMSIN MEDICA</span>
  </div>
  <div class="lens" role="img" aria-label="Intraocular lens with haptics"></div>
  <div class="warnings">
    <p>Contains one sterile intraocular lens<br>Do not use if the packaging is damaged<br>Do not resterilize</p>
    <p>Bevat één steriele intraoculaire lens<br>Niet gebruiken als de verpakking beschadigd is<br>Niet opnieuw steriliseren</p>
    <p>Contient une lentille intraoculaire stérile<br>Ne pas utiliser si l'emballage est endommagé<br>Ne pas restériliser</p>
    <p>Enthält eine sterile Intraokulare Linse<br>Nicht verwenden, wenn die Verpackung beschädigt ist<br>Nicht resterilisieren</p>
    <p>Περιέχει ένα αποστειρωμένο ενδοφθάλμιο φακό<br>Μην το χρησιμοποιείτε εάν η συσκευασία έχει υποστεί ζημιά<br>Μην επαναποστειρώνετε</p>
    <p>Contiene una lente intraoculare sterile<br>Non usare se la confezione è danneggiata<br>Non risterilizzare</p>
    <p>Contém uma lente intra-ocular esterilizada<br>Não use se a embalagem está danificada<br>Não reesterilize</p>
    <p>Contiene una lente intraocular estéril<br>No utilizar si el envase está dañado<br>No vuelva a esterilizar</p>
  </div>
  <div class="symbols">
    <div class="sterile"><span>STERILE</span><span>EO</span></div>
    <svg width="16" height="14" viewBox="0 0 16 14"><path d="M8 1 L15 13 H1 Z" fill="none" stroke="#2a2a2a"/><line x1="8" y1="5" x2="8" y2="9" stroke="#2a2a2a"/></svg>
    <svg width="14" height="14" viewBox="0 0 14 14"><circle cx="7" cy="7" r="6" fill="none" stroke="#2a2a2a"/><line x1="3" y1="11" x2="11" y2="3" stroke="#2a2a2a"/></svg>
    <svg width="14" height="14" viewBox="0 0 14 14"><circle cx="7" cy="7" r="6" fill="none" stroke="#2a2a2a"/><line x1="3" y1="3" x2="11" y2="11" stroke="#2a2a2a"/></svg>
    <svg width="14" height="14" viewBox="0 0 14 14"><circle cx="7" cy="7" r="6" fill="none" stroke="#2a2a2a"/><circle cx="7" cy="7" r="3" fill="none" stroke="#2a2a2a"/></svg>
  </div>
</section>

<section class="panel panel--front" aria-label="Front panel">
  <div class="pattern"></div>
  <h2 class="title">HYDROPHOBIC INTRAOCULAR LENS</h2>
  <div class="brand">
    <span class="brand__ring"></span>
    <span class="brand__name">TAMSIN MEDICA</span>
  </div>
  <div class="lens" role="img" aria-label="Intraocular lens with haptics, enlarged"></div>
  <div class="product">
    <div class="product__name">VENOR</div>
    <div class="product__type">ASPHERIC WITH 360° LENS</div>
  </div>
</section>

</body>
</html>
```